Salon and Spa Distributor Business Card

Need a business card. We are are distributor in the salon and spa industry. We identify with natural beauty. Need a card with:
Company Name: Petal Haven"
Title: "President & CEO"
Address
Company Phone number
email
website
Tag Line:" Naturally Beautiful Salon Supply"

Industry/Entity Type

Business

Contact Information for Business Card

Name: Lena Morcott
Title: "President & CEO"
Address: 317 Birchfield Ln, Oakvane, NJ 07481
Company Phone number: 800-463-9152
email: lenamorcott@petalhaven-example.com
website: www.petalhaven-example.com

Requirements
Should not have
• No black backgrounds

```html
<!DOCTYPE html>
<html lang="en">
<head>
<meta charset="utf-8">
<title>Petal Haven — Business Card</title>
<link rel="stylesheet" href="https://fonts.googleapis.com/css2?family=Questrial&family=Montserrat:wght@700&display=swap">
<style>
  :root {
    --canvas-bg: #ecece9;
    --card-bg: #ffffff;
    --green: #5bb53f;
    --green-dark: #1f8a3c;
    --brand-green: #4a9a45;
    --ink: #2b2b2b;
    --ink-soft: #4a4a4a;
    --divider: #8c8c8c;
  }
  * { box-sizing: border-box; margin: 0; padding: 0; }
  html, body { width: 1200px; height: 1000px; overflow: hidden; }
  body {
    background: var(--canvas-bg);
    font-family: "Questrial", "Century Gothic", sans-serif;
    position: relative;
  }
  .card {
    position: absolute;
    background: var(--card-bg);
    border-radius: 22px;
    box-shadow: 0 6px 18px rgba(0,0,0,0.12);
    overflow: hidden;
  }

  /* Front card */
  .card--front { left: 110px; top: 130px; width: 580px; height: 325px; }
  .front-brand {
    position: absolute; left: 40px; top: 70px; width: 210px;
    display: flex; flex-direction: column; align-items: center; gap: 18px;
  }
  .brand-dot { width: 96px; height: 96px; border-radius: 50%; background: var(--green); }
  .brand-name {
    color: var(--brand-green); font-size: 24px; font-weight: 400; white-space: nowrap;
  }
  .front-divider {
    position: absolute; left: 268px; top: 42px; width: 1px; height: 168px;
    background: var(--divider);
  }
  .front-details { position: absolute; left: 290px; top: 38px; width: 280px; }
  .person-name {
    font-family: "Montserrat", sans-serif; font-weight: 700; font-size: 22px;
    color: var(--ink); line-height: 1.1;
  }
  .person-name .surname { color: var(--green); }
  .person-title { font-size: 16px; color: var(--ink); margin: 3px 0 12px; }
  .contact-list { list-style: none; }
  .contact-item {
    display: flex; align-items: flex-start; gap: 8px;
    font-size: 13px; color: var(--ink-soft); line-height: 1.35; margin-bottom: 3px;
    white-space: nowrap;
  }
  .contact-item svg { flex: 0 0 13px; margin-top: 2px; }
  .tagline-band {
    position: absolute; left: 0; right: 0; top: 250px; height: 40px;
    background: linear-gradient(90deg, var(--green-dark), var(--green) 60%, #66c245);
    display: flex; align-items: center; padding-left: 160px;
  }
  .tagline { color: #fff; font-size: 17px; letter-spacing: 0.2px; white-space: nowrap; }

  /* Back card */
  .card--back { left: 515px; top: 520px; width: 520px; height: 295px; }
  .back-brand {
    position: absolute; inset: 0;
    display: flex; align-items: center; justify-content: center; gap: 26px;
  }
  .back-brand .brand-dot { width: 120px; height: 120px; }
  .back-brand .brand-name { font-size: 42px; }
</style>
</head>
<body>

  <section class="card card--front" aria-label="Business card front">
    <div class="front-brand">
      <span class="brand-dot" aria-hidden="true"></span>
      <span class="brand-name">Petal Haven</span>
    </div>

    <div class="front-divider"></div>

    <div class="front-details">
      <h1 class="person-name">Lena <span class="surname">Morcott</span></h1>
      <p class="person-title">President &amp; CEO</p>
      <ul class="contact-list">
        <li class="contact-item">
          <svg width="13" height="13" viewBox="0 0 24 24" aria-hidden="true"><path fill="#5bb53f" d="M6.6 10.8a15 15 0 0 0 6.6 6.6l2.2-2.2a1 1 0 0 1 1-.25 11.4 11.4 0 0 0 3.6.57 1 1 0 0 1 1 1V20a1 1 0 0 1-1 1A17 17 0 0 1 3 4a1 1 0 0 1 1-1h3.5a1 1 0 0 1 1 1c0 1.250.2 2.450.57 3.57a1 1 0 0 1-.25 1z"/></svg>
          <span>800 - 463 - 9152</span>
        </li>
        <li class="contact-item">
          <svg width="13" height="13" viewBox="0 0 24 24" aria-hidden="true"><rect x="2" y="5" width="20" height="14" rx="2" fill="#5bb53f"/><path d="M3 6l9 7 9-7" stroke="#fff" stroke-width="2" fill="none"/></svg>
          <span>lenamorcott@petalhaven-example.com</span>
        </li>
        <li class="contact-item">
          <svg width="13" height="13" viewBox="0 0 24 24" aria-hidden="true"><circle cx="12" cy="12" r="10" fill="#5bb53f"/><g stroke="#fff" stroke-width="1.5" fill="none"><ellipse cx="12" cy="12" rx="4" ry="10"/><path d="M2 12h20M4 7h16M4 17h16"/></g></svg>
          <span>www.petalhaven-example.com</span>
        </li>
        <li class="contact-item">
          <svg width="13" height="13" viewBox="0 0 24 24" aria-hidden="true"><path fill="#5bb53f" d="M12 2a7 7 0 0 0-7 7c0 5 7 13 7 13s7-8 7-13a7 7 0 0 0-7-7z"/><circle cx="12" cy="9" r="2.6" fill="#fff"/></svg>
          <span>317 Birchfield Ln<br>Oakvane, NJ 07481</span>
        </li>
      </ul>
    </div>

    <div class="tagline-band">
      <p class="tagline">“Naturally Beautiful Salon Supply”</p>
    </div>
  </section>

  <section class="card card--back" aria-label="Business card back">
    <div class="back-brand">
      <span class="brand-dot" aria-hidden="true"></span>
      <span class="brand-name">Petal Haven</span>
    </div>
  </section>

</body>
</html>
```